Brantley Roofing needs redesign of vehicle graphics

We are wanting to redesign our Brantley Roofing vehicle graphics to a wrap. We are wanting this design to be eye catching while it lets people know about our business and what we offer. We would like to use our logo, maybe shingles in the background with our information that is currently being used on the truck. I would like to keep royal blues, grays and black. We really like how the Dornick Roofing truck looks & want ours to be like it with our information. Tag line: Exceptional Roofs. Extraordinary Service.

Target Market(s)

homeowners & businesses

Industry/Entity Type

Roofing Contractor

Font styles to use
Other font styles liked:
• Courgette, Satisfy, Nexa Script

Colors
0054AA
0677BA
7BADD7
CADEEF
E8F1F8

Requirements
Must have
• Residential & Commercial, Free Estimates, Financing Available, 785-316-8027, brantleyroofingllc.example, our QR code
Nice to have
• The Dornick Roofing truck images that are uploaded is a look we like.
Should not have
• Storms or lightning!!! things that are not roofing related, random colors & designs

```html
<!DOCTYPE html>
<html lang="en">
<head>
<meta charset="utf-8">
<title>Brantley Roofing – Vehicle Wrap Layout</title>
<link href="https://fonts.googleapis.com/css2?family=Playfair+Display:wght@700;800&display=swap" rel="stylesheet">
<style>
  :root {
    --backdrop: #d3d4d6;
    --sky-light: #86b3e6;
    --sky-deep: #4683c9;
    --ridge: #0b0b0b;
    --ridge-soft: #1c1c1c;
    --figure-top: #2a2a2a;
    --figure-bottom: #0b0b0b;
    --ink: #0a0a0a;
    --silver: #c8c9cb;
    --qr-field: #e6e7e9;
  }
  html, body {
    margin: 0;
    padding: 0;
    width: 840px;
    height: 1200px;
    overflow: hidden;
    background: var(--backdrop);
  }
  .canvas {
    width: 840px;
    height: 1200px;
    display: block;
  }
  .wrap-text {
    font-family: "Playfair Display", Georgia, serif;
    font-weight: 800;
  }
  .phone { fill: var(--ink); }
  .company { fill: var(--silver); }
  .services { fill: var(--silver); font-weight: 700; }
  .offers { fill: var(--silver); font-weight: 700; letter-spacing: 0.5px; }
  .website { fill: var(--silver); font-weight: 700; font-variant: small-caps; }
  .ridge { fill: var(--ridge); }
  .ridge-band { fill: var(--ridge-soft); }
  .panel-edge { fill: none; stroke: #9a9ca0; stroke-width: 1; }
  .qr-area { fill: var(--qr-field); }
</style>
</head>
<body>
<svg class="canvas" viewBox="0 0 840 1200" xmlns="http://www.w3.org/2000/svg">
  <defs>
    <linearGradient id="sky" x1="0" y1="0" x2="0" y2="1">
      <stop offset="0" stop-color="var(--sky-light)"/>
      <stop offset="1" stop-color="var(--sky-deep)"/>
    </linearGradient>
    <linearGradient id="figure-fill" x1="0" y1="0" x2="0" y2="1">
      <stop offset="0" stop-color="var(--figure-top)"/>
      <stop offset="1" stop-color="var(--figure-bottom)"/>
    </linearGradient>
  </defs>

  <!-- Driver side panel -->
  <g class="side-panel side-driver" transform="translate(40,60)">
    <rect width="760" height="210" rx="14" fill="url(#sky)"/>
    <path class="ridge" d="M0 150 L60 138 L130 128 L200 140 L270 132 L340 126 L400 118 L470 112 L540 106 L600 112 L660 110 L720 104 L760 100 L760 196 Q760 210 746 210 L14 210 Q0 210 0 196 Z"/>
    <rect class="ridge-band" x="350" y="160" width="360" height="6"/>
    <rect class="roofer-area" x="232" y="40" width="106" height="170" rx="10" fill="url(#figure-fill)" role="img" aria-label="Silhouette of a roofer kneeling on a roof with a hammer"/>
    <text class="wrap-text phone" x="34" y="68" font-size="29" textLength="172" lengthAdjust="spacingAndGlyphs">785.316.8027</text>
    <text class="wrap-text website" x="42" y="86" font-size="13" textLength="156" lengthAdjust="spacingAndGlyphs">BrantleyRoofingLLC.example</text>
    <text class="wrap-text company" x="352" y="98" font-size="27" textLength="330" lengthAdjust="spacingAndGlyphs">BRANTLEY ROOFING LLC</text>
    <text class="wrap-text services" x="360" y="184" font-size="16" textLength="236" lengthAdjust="spacingAndGlyphs">RESIDENTIAL &amp; COMMERCIAL</text>
    <rect class="panel-edge" width="760" height="210" rx="14"/>
  </g>

  <!-- Passenger side panel -->
  <g class="side-panel side-passenger" transform="translate(40,380)">
    <rect width="760" height="210" rx="14" fill="url(#sky)"/>
    <path class="ridge" d="M0 100 L40 104 L100 110 L160 106 L220 112 L290 118 L360 126 L430 132 L490 140 L560 128 L630 138 L700 142 L760 148 L760 196 Q760 210 746 210 L14 210 Q0 210 0 196 Z"/>
    <rect class="ridge-band" x="50" y="160" width="410" height="6"/>
    <rect class="roofer-area" x="478" y="40" width="88" height="170" rx="10" fill="url(#figure-fill)" role="img" aria-label="Silhouette of a roofer kneeling on a roof with a hammer"/>
    <text class="wrap-text company" x="130" y="98" font-size="27" textLength="330" lengthAdjust="spacingAndGlyphs">BRANTLEY ROOFING LLC</text>
    <text class="wrap-text services" x="196" y="184" font-size="16" textLength="236" lengthAdjust="spacingAndGlyphs">RESIDENTIAL &amp; COMMERCIAL</text>
    <text class="wrap-text phone" x="574" y="68" font-size="29" textLength="172" lengthAdjust="spacingAndGlyphs">785.316.8027</text>
    <text class="wrap-text website" x="582" y="86" font-size="13" textLength="156" lengthAdjust="spacingAndGlyphs">BrantleyRoofingLLC.example</text>
    <rect class="panel-edge" width="760" height="210" rx="14"/>
  </g>

  <!-- Tailgate panel -->
  <g class="tailgate-panel" transform="translate(100,700)">
    <rect width="620" height="250" rx="10" fill="url(#sky)"/>
    <path class="ridge" d="M0 112 L60 106 L130 98 L190 104 L260 108 L330 104 L390 112 L450 120 L520 124 L580 128 L620 132 L620 240 Q620 250 610 250 L10 250 Q0 250 0 240 Z"/>
    <rect class="ridge-band" x="0" y="120" width="460" height="6" opacity="0.6"/>
    <rect class="roofer-area" x="466" y="22" width="130" height="150" rx="10" fill="url(#figure-fill)" role="img" aria-label="Silhouette of a roofer kneeling on a roof with a hammer"/>
    <text class="wrap-text phone" x="44" y="52" font-size="30" textLength="196" lengthAdjust="spacingAndGlyphs">785.316.8027</text>
    <text class="wrap-text company" x="88" y="98" font-size="30" textLength="360" lengthAdjust="spacingAndGlyphs">BRANTLEY ROOFING LLC</text>
    <text class="wrap-text website" x="206" y="154" font-size="16" textLength="196" lengthAdjust="spacingAndGlyphs">BrantleyRoofingLLC.example</text>
    <text class="wrap-text services" x="134" y="190" font-size="22" textLength="340" lengthAdjust="spacingAndGlyphs">RESIDENTIAL &amp; COMMERCIAL</text>
    <text class="wrap-text offers" x="180" y="224" font-size="13" textLength="250" lengthAdjust="spacingAndGlyphs">FREE ESTIMATES • FINANCING AVAILABLE</text>
    <rect class="qr-area" x="28" y="160" width="64" height="64" rx="4" role="img" aria-label="QR code linking to the company website"/>
    <rect class="panel-edge" width="620" height="250" rx="10"/>
  </g>
</svg>
</body>
</html>
```